E-book cover required. Title is Oda, author Clara J Penrod. Would like large title at top and smaller name at bottom. Book is apocolyptic novel and design needs to reference blood. Simple would be best.

```html
<!DOCTYPE html>
<html lang="en">
<head>
<meta charset="UTF-8">
<title>Oda — Clara J Penrod</title>
<link rel="stylesheet" href="https://fonts.googleapis.com/css2?family=League+Spartan:wght@600;700&display=swap">
<style>
  :root {
    --ink: #000000;
    --paper: #ffffff;
    --blood: #8b0a0c;
    --blood-deep: #6e0507;
  }
  html, body {
    margin: 0;
    padding: 0;
    width: 750px;
    height: 1200px;
    overflow: hidden;
    background: var(--ink);
  }
  .cover {
    position: relative;
    width: 750px;
    height: 1200px;
    background: var(--ink);
    overflow: hidden;
    font-family: "League Spartan", sans-serif;
  }
  .cover-art {
    position: absolute;
    inset: 0;
    width: 750px;
    height: 1200px;
  }
  .title-text {
    font-family: "League Spartan", sans-serif;
    font-weight: 700;
    font-size: 430px;
    fill: var(--paper);
  }
  .author {
    position: absolute;
    left: 0;
    right: 0;
    top: 1036px;
    margin: 0;
    text-align: center;
    font-weight: 600;
    font-size: 70px;
    line-height: 1;
    letter-spacing: 1px;
    text-transform: uppercase;
    white-space: nowrap;
  }
  .author-first { color: var(--blood); }
  .author-last { color: var(--paper); }
</style>
</head>
<body>
<main class="cover">
  <svg class="cover-art" viewBox="0 0 750 1200" xmlns="http://www.w3.org/2000/svg">
    <defs>
      <radialGradient id="splash-title" cx="0.55" cy="0.4" r="0.6">
        <stop offset="0" stop-color="var(--blood)" stop-opacity="0.95"/>
        <stop offset="0.6" stop-color="var(--blood)" stop-opacity="0.55"/>
        <stop offset="1" stop-color="var(--blood)" stop-opacity="0"/>
      </radialGradient>
      <radialGradient id="splash-band" cx="0.2" cy="0.5" r="0.8">
        <stop offset="0" stop-color="var(--blood-deep)" stop-opacity="0.95"/>
        <stop offset="0.55" stop-color="var(--blood)" stop-opacity="0.6"/>
        <stop offset="1" stop-color="var(--blood)" stop-opacity="0"/>
      </radialGradient>
      <clipPath id="title-shape">
        <text class="title-text" x="68" y="322" textLength="600" lengthAdjust="spacingAndGlyphs">ODA</text>
      </clipPath>
      <clipPath id="band-shape">
        <polygon points="0,570 750,327 750,645 0,885"/>
      </clipPath>
    </defs>

    <text class="title-text" x="68" y="322" textLength="600" lengthAdjust="spacingAndGlyphs">ODA</text>
    <g clip-path="url(#title-shape)" role="img" aria-label="Blood splatter across the last letter of the title">
      <ellipse cx="600" cy="140" rx="150" ry="190" fill="url(#splash-title)"/>
    </g>

    <polygon class="band" points="0,570 750,327 750,645 0,885" fill="var(--paper)"/>
    <g clip-path="url(#band-shape)" role="img" aria-label="Blood splatter on the left end of the white band">
      <ellipse cx="90" cy="700" rx="260" ry="180" fill="url(#splash-band)"/>
    </g>
  </svg>

  <h2 class="author"><span class="author-first">Clara J</span> <span class="author-last">Penrod</span></h2>
</main>
</body>
</html>
```